HarborLoop - Shore Excursions Operator Software Trade show pop-up display

Create Trade show Pop-up banners Suitable for printing at 33.5 inches by 80 inches high. I have included a description of what our software does. We are at a trade show focusing on acquiring tour operators to sign up and use our software. This specifically is built for cruise line markets. I am uploading two versions of our logo, one is just a simple version the other is the name spelled out. We want to include both because as a new company the branding identity is not very strong with the simple logo. The image I'm uploading is a backdrop with the cruise ship is what we use for our back image on the customer facing website. I am also uploading some screenshots of our software which is designed for desktop, tablet, and mobile. I want to be provocative and enticing and somewhat cutting edge but certainly to be driven towards the cruise industry and tour operators who work with the cruise industry specifically. I also uploaded an example of a chatgpt display for reference as to what we are looking for (but not that image specifically).
HarborLoop Software Overview for Designers
Purpose of the Software:
HarborLoop is an all-in-one operating system for shore excursion tour operators. It connects directly with cruise lines, manages every part of tour operations, and helps operators maximize revenue while reducing manual work.
The software is designed for companies that provide tours, transportation, and shore excursions for cruise ship passengers. Operators use HarborLoop to run their entire business — from inventory management to daily dispatch.
Key Value in Simple Terms
Maximize Revenue → By syncing with cruise ship schedules, managing contracts, invoicing, and reallocating inventory in real time.
Operational Control → From assigning guides and vehicles to monitoring maintenance and scheduling daily tours automatically.
Simplify Bookings → Manage bookings from cruise lines, travel agents, and direct guests in one hub.
Smarter Management → Staff, inventory, contracts, and content are centralized for full visibility and efficiency.
Future-Proof → Analytics, reporting, and scalability ensure operators grow alongside cruise line demand.
What HarborLoop Does (Modules & Functions)
1. Cruise Line & Revenue Management
Real-time cruise calendars
Pricing & contract management
Automated invoicing for cruise lines
Faster release of inventory for sales
Visual cues for design: 📅 Calendar icons, 💰 revenue charts, 📄 contract documents.
2. Inventory & Allocation
Central hub for inventory (direct sales, cruise lines, individual ships)
Automatic capacity alerts (when seats run low)
Bulk uploads of sales data (hundreds of hours saved)
Demand-based allocation for higher yield
Visual cues: 🚍 Bus seats filling up, ⚠️ alerts, ⬆️ demand graphs.
3. Booking & Guest Management
Unified booking system (cruise lines, agents, direct guests)
Integrated payments & invoices
Guest management for changes, cancellations, special requests
Agent & affiliate campaign tools
Visual cues: 🎟 tickets, 🧑🤝🧑 guest icons, 💳 payment/booking screens.
4. Daily Tour Dispatch (DTD)
Generates real-time daily tour schedule
Assigns guides, drivers, and vehicles automatically
Tracks guest counts & departures live
Mobile access for staff & guides
Visual cues: 🚌 bus/tour icons, 📱 mobile access, ✅ checklist/schedule view.
5. Fleet & Maintenance
Live fleet tracking (location, activity, mileage)
Inspection & maintenance reports
Photo/video upload for repair tracking
Visual cues: 🚐 vehicles, 🔧 maintenance tools, 📍 GPS markers.
6. Employee & Staff Management
Track certifications, training, and staff profiles
Assign roles, shifts, and responsibilities
Proactive alerts for expired credentials
Visual cues: 🧑✈️ staff badges, 🎓 training icons, 👤 profile cards.
7. Content & Branding Control
Manage all tour content (descriptions, itineraries, FAQs, images, videos)
Apply refund policies & contracted rates
Ensure consistent, accurate guest-facing info
Visual cues: 🖼 images, 📝 itinerary lists, 🌐 consistent branding.
8. Analytics & Future-Proofing
Sales reporting by ship, departure, and channel
Historic vs. future pricing analysis
Scalable platform that grows with the operator
Visual cues: 📊 dashboards, 📈 performance charts, 🔮 forward-looking visuals.
Overall Design Themes to Convey
Smart, seamless, and connected. (No clutter, everything integrated.)
Professional + trustworthy. (Executive decision-makers are the audience.)
Cruise-specific but modern. (Avoid cliché palm trees; instead, ships, schedules, people, and data visuals.)
Dynamic and active. (Show energy — tours, departures, real-time control.)

```html
<!DOCTYPE html>
<html lang="en">
<head>
<meta charset="utf-8">
<title>HarborLoop – Trade Show Pop-up Banner</title>
<link rel="stylesheet" href="https://fonts.googleapis.com/css2?family=Poppins:wght@700;800&family=Roboto:wght@400;500;700&display=swap">
<style>
  :root {
    --navy: #073a5e;
    --text-dark: #183449;
    --white: #ffffff;
    --stage: #8f8f8f;
  }
  * { box-sizing: border-box; margin: 0; padding: 0; }
  html, body { width: 1200px; height: 2420px; overflow: hidden; background: var(--stage); }
  .banner {
    position: absolute; left: 100px; top: 15px;
    width: 1000px; height: 2390px; overflow: hidden;
    background: var(--white);
    font-family: "Roboto", Arial, sans-serif;
  }
  .banner-art { position: absolute; inset: 0; width: 1000px; height: 2390px; }
  .wordmark {
    position: absolute; left: 0; right: 0; top: 52px;
    text-align: center;
    font-family: "Poppins", Arial, sans-serif; font-weight: 800;
    font-size: 96px; letter-spacing: 1px; line-height: 1;
    color: var(--navy);
  }
  .section-tab {
    position: absolute; left: 180px; top: 166px; width: 640px; height: 112px;
    background: var(--navy); color: var(--white);
    border-radius: 72px 0 72px 0;
    display: flex; align-items: center; justify-content: center;
    font-family: "Poppins", Arial, sans-serif; font-weight: 800; font-size: 40px;
    letter-spacing: -0.3px;
  }
  .module { position: absolute; display: flex; align-items: center; }
  .module-icon {
    width: 114px; height: 114px; border-radius: 50%;
    background: var(--white);
    box-shadow: 0 4px 14px rgba(10, 40, 70, 0.18);
    display: flex; align-items: center; justify-content: center;
    flex-shrink: 0;
  }
  .module-icon svg { width: 56px; height: 56px; fill: var(--navy); }
  .module-label {
    margin-left: 18px; font-size: 29px; font-weight: 500; line-height: 36px;
    color: var(--text-dark); white-space: nowrap;
  }
  .value-heading {
    position: absolute; left: 97px; top: 1421px;
    font-family: "Poppins", Arial, sans-serif; font-weight: 800;
    font-size: 40px; line-height: 46px; color: var(--white);
  }
  .value-item { position: absolute; left: 112px; width: 860px; color: var(--white); }
  .value-bullet {
    position: absolute; left: 0; top: 8px; width: 64px; height: 40px;
    border-radius: 50%; border: 6px solid var(--white);
  }
  .value-title { margin-left: 101px; font-weight: 700; font-size: 28px; line-height: 34px; }
  .value-text {
    margin-left: 101px; margin-top: 6px; font-size: 24px; line-height: 32px;
    white-space: nowrap;
  }
  .cta {
    position: absolute; left: 108px; top: 2309px; width: 742px; height: 90px;
    background: var(--white); border-radius: 48px 48px 0 0;
    display: flex; align-items: center; justify-content: center;
    font-family: "Poppins", Arial, sans-serif; font-weight: 700; font-size: 42px;
    color: var(--navy);
  }
</style>
</head>
<body>
<main class="banner">
  <svg class="banner-art" viewBox="0 0 1000 2390">
    <defs>
      <linearGradient id="skyFade" x1="0" y1="0" x2="0" y2="1">
        <stop offset="0" stop-color="#c6dde9"/>
        <stop offset="0.12" stop-color="#e6f0f5"/>
        <stop offset="0.22" stop-color="#ffffff"/>
        <stop offset="1" stop-color="#ffffff"/>
      </linearGradient>
      <linearGradient id="seaTone" x1="0" y1="0" x2="0.4" y2="1">
        <stop offset="0" stop-color="#10507a"/>
        <stop offset="0.45" stop-color="#2b8fb5"/>
        <stop offset="0.7" stop-color="#0c4d74"/>
        <stop offset="1" stop-color="#073a5e"/>
      </linearGradient>
      <linearGradient id="sunsetTone" x1="0" y1="0" x2="0" y2="1">
        <stop offset="0" stop-color="#ffffff"/>
        <stop offset="0.18" stop-color="#dfe5ee"/>
        <stop offset="0.38" stop-color="#e9b69a"/>
        <stop offset="0.52" stop-color="#d9895f"/>
        <stop offset="0.68" stop-color="#c9cfd8"/>
        <stop offset="0.82" stop-color="#5d7c98"/>
        <stop offset="1" stop-color="#27486a"/>
      </linearGradient>
    </defs>
    <rect class="sky-backdrop" x="0" y="0" width="1000" height="900" fill="url(#skyFade)"/>
    <rect class="sea-backdrop" x="0" y="790" width="1000" height="1600" fill="url(#seaTone)"/>
    <rect class="footer-field" x="0" y="1571" width="1000" height="819" fill="#073a5e"/>
    <path class="ship-photo" role="img" aria-label="Cruise ship sailing on open sea under a sunset sky"
          d="M0,700 L1000,700 L1000,1477 C600,1482 220,1250 0,805 Z" fill="url(#sunsetTone)"/>
    <path class="white-swoosh" d="M0,790 C120,1180 470,1578 1000,1571 L1000,1477 C600,1482 220,1250 0,805 Z" fill="#ffffff"/>
  </svg>

  <div class="wordmark">HARBORLOOP</div>
  <div class="section-tab">WHAT HARBORLOOP DOES</div>

  <div class="module" style="left:110px; top:334px;">
    <div class="module-icon"><svg viewBox="0 0 48 48"><path d="M21 6h6v5h-6z M14 13h20v9l-10-4-10 4z M6 26l18-7 18 7-4 11H10z M4 40c4 0 6-2 10-2s6 2 10 2 6-2 10-2 6 2 10 2v3c-4 0-6-2-10-2s-6 2-10 2-6-2-10-2-6 2-10 2z"/></svg></div>
    <div class="module-label">Cruise Line &amp;<br>Revenue<br>Management</div>
  </div>
  <div class="module" style="left:551px; top:334px;">
    <div class="module-icon"><svg viewBox="0 0 48 48"><path d="M14 12h5v5h-5z M20 10h5v7h-5z M10 18h26v6H10z M2 25h44l-6 11H7z M6 39c4 0 5-2 9-2s5 2 9 2 5-2 9-2 5 2 9 2v3c-4 0-5-2-9-2s-5 2-9 2-5-2-9-2-5 2-9 2z"/></svg></div>
    <div class="module-label">Fleet &amp;<br>Maintenance</div>
  </div>
  <div class="module" style="left:110px; top:510px;">
    <div class="module-icon"><svg viewBox="0 0 48 48"><path d="M17 4h14v16H17z M4 24h18v20H4z M26 24h18v20H26z"/></svg></div>
    <div class="module-label">Inventory &amp;<br>Allocation</div>
  </div>
  <div class="module" style="left:551px; top:510px;">
    <div class="module-icon"><svg viewBox="0 0 48 48"><circle cx="24" cy="12" r="7"/><circle cx="10" cy="17" r="5"/><circle cx="38" cy="17" r="5"/><path d="M14 42V30a10 10 0 0 1 20 0v12z M2 42V32a8 8 0 0 1 10-7v17z M46 42V32a8 8 0 0 0-10-7v17z"/></svg></div>
    <div class="module-label">Employee &amp;<br>Staff Management</div>
  </div>
  <div class="module" style="left:110px; top:685px;">
    <div class="module-icon"><svg viewBox="0 0 48 48"><path d="M12 4h4v6h-4z M32 4h4v6h-4z M6 8h36v34H6z M10 18v20h28V18z"/><path d="M16 27l6 6 11-11" fill="none" stroke="#073a5e" stroke-width="3.5"/></svg></div>
    <div class="module-label">Booking &amp; Guest<br>Management</div>
  </div>
  <div class="module" style="left:551px; top:685px;">
    <div class="module-icon"><svg viewBox="0 0 48 48"><path d="M21 2h6l1 6 5 2 5-4 4 4-4 5 2 5 6 1v6l-6 1-2 5 4 5-4 4-5-4-5 2-1 6h-6l-1-6-5-2-5 4-4-4 4-5-2-5-6-1v-6l6-1 2-5-4-5 4-4 5 4 5-2z"/><circle cx="24" cy="24" r="10" fill="#fff"/><circle cx="24" cy="24" r="7"/><path d="M20 24l3 3 5-6" fill="none" stroke="#fff" stroke-width="2.5"/></svg></div>
    <div class="module-label">Content &amp; Branding<br>Control</div>
  </div>
  <div class="module" style="left:110px; top:860px;">
    <div class="module-icon"><svg viewBox="0 0 48 48"><path d="M18 2h12v6H18z M8 6h8v4h16V6h8v40H8z"/><path d="M14 18l2 2 3-3 M14 27l2 2 3-3 M14 36l2 2 3-3 M23 19h11 M23 28h11 M23 37h11" fill="none" stroke="#fff" stroke-width="2.5"/></svg></div>
    <div class="module-label">Daily Tour<br>Dispatch (DTD)</div>
  </div>
  <div class="module" style="left:551px; top:860px;">
    <div class="module-icon"><svg viewBox="0 0 48 48"><path d="M6 30h6v14H6z M16 24h6v20h-6z M26 28h6v16h-6z M36 18h6v26h-6z"/><path d="M6 22l10-8 10 6 14-12" fill="none" stroke="#073a5e" stroke-width="3"/><path d="M36 4h8v8z"/></svg></div>
    <div class="module-label">Analytics &amp;<br>Future-Proofing</div>
  </div>

  <h2 class="value-heading">KEY VALUE<br>IN SIMPLE TERMS</h2>

  <div class="value-item" style="top:1598px;">
    <span class="value-bullet"></span>
    <div class="value-title">Maximize Revenue</div>
    <div class="value-text">By syncing with cruise ship schedules, managing contracts,<br>invoicing, and reallocating inventory in real time.</div>
  </div>
  <div class="value-item" style="top:1741px;">
    <span class="value-bullet"></span>
    <div class="value-title">Operational Control</div>
    <div class="value-text">From assigning guides and vehicles to monitoring maintenance<br>and scheduling daily tours automatically.</div>
  </div>
  <div class="value-item" style="top:1885px;">
    <span class="value-bullet"></span>
    <div class="value-title">Simplify Bookings</div>
    <div class="value-text">Manage bookings from cruise lines, travel agents, and direct<br>guests in one hub.</div>
  </div>
  <div class="value-item" style="top:2028px;">
    <span class="value-bullet"></span>
    <div class="value-title">Smarter Management</div>
    <div class="value-text">Staff, inventory, contracts, and content are centralized for<br>full visibility and efficiency.</div>
  </div>
  <div class="value-item" style="top:2164px;">
    <span class="value-bullet"></span>
    <div class="value-title">Future-Proof</div>
    <div class="value-text">Analytics, reporting, and scalability ensure operators grow<br>alongside cruise line demand.</div>
  </div>

  <div class="cta">HarborLoop.Com</div>
</main>
</body>
</html>
```